We are the world's leading center for transgender surgery and have multiple locations.

We want a unique and dynamic business card that wows potential patients and referral sources (physicians, previous patients, etc). We are open to inventive designs, card shape, additional design on the back of the card, etc.

We are a surgical practice in a competitive environment and want to stand out as the leader in transgender surgery. We have multiple surgeons with unique talents who are impeccably trained with extensive experience. We are dedicated to our patients and their needs. We want the card to stand out and impress them. We want it to be suitable to all of the surgeons as well as our staff.

Our practice started as a small practice in San Francisco, CA and now has an additional location in Austin Texas (as well as another city to be announced later). Our practice has plastic surgeons, reconstructive urologists, general surgeons and gynecologists.

We continue to boast some of the lowest published phalloplasty complication rates in the world and our San Francisco microsurgeons that we have been working with for more than a year and a half have 0 microvascular take backs and 0 flap failures. Between our two centers in San Francisco, California and Austin, Texas, we perform 5-6 phalloplasties per week, making us one of the largest volume centers in the world.

Target Market(s)

Potential Transgender patients (all genders) and referring physicians

Industry/Entity Type

Surgeon

Contact Information for Business Card

Here is an example of one of our physicians:

Daniel R. Venko, MD
Reconstructive Urology for the Transgender Community
Diplomate, National Council of Renal Medicine with subspecialty certification in FPS and Reconstructive Surgery

812 Orchard Vale Rd
Suite 4
Larkmoor, CA 94917

phone 628-738-2914
fax 628-592-8167

Font styles to use
Sans Serif

Requirements
Must have
• Must have a unique look, but tasteful.
Nice to have
• ?
Should not have
• ?

```html
<!DOCTYPE html>
<html lang="en">
<head>
<meta charset="utf-8">
<title>Heron Center — Business Card</title>
<link href="https://fonts.googleapis.com/css2?family=Arimo:wght@700&family=Open+Sans:wght@400&display=swap" rel="stylesheet">
<style>
  :root {
    --backdrop: #d2d3d5;
    --paper: #ffffff;
    --magenta: #a31f6a;
    --navy: #22336e;
    --edge: #8e8f93;
  }
  * { margin: 0; padding: 0; box-sizing: border-box; }
  html, body { width: 1126px; height: 1200px; overflow: hidden; }
  body { background: var(--backdrop); position: relative; font-family: "Open Sans", sans-serif; }

  .card {
    position: absolute; left: 200px; width: 726px;
    background: var(--paper);
    border: 1px solid var(--edge);
    border-radius: 32px;
    overflow: hidden;
  }
  .card--front { top: 161px; height: 424px; }
  .card--back  { top: 634px; height: 417px; }

  .brand {
    position: absolute; left: 166px; height: 120px;
    display: flex; align-items: center; gap: 14px;
  }
  .card--front .brand { top: 29px; }
  .card--back .brand { top: 76px; }
  .brand__dot { width: 116px; height: 116px; border-radius: 50%; background: var(--navy); flex: none; }
  .brand__name {
    font-family: "Arimo", sans-serif; font-weight: 700;
    font-size: 40px; letter-spacing: -0.5px; color: var(--magenta);
    text-transform: uppercase; white-space: nowrap;
  }

  .person { position: absolute; left: 0; right: 0; text-align: center; font-family: "Arimo", sans-serif; font-weight: 700; line-height: 1; }
  .person__name { top: 198px; font-size: 26px; color: var(--magenta); text-transform: uppercase; }
  .person__name small { font-size: 18px; }
  .person__role { top: 228px; font-size: 20px; color: var(--navy); }

  .rule { position: absolute; left: 0; right: 0; height: 5px; background: var(--navy); }
  .band { position: absolute; left: 0; right: 0; bottom: 0; background: var(--magenta); }
  .card--front .rule { top: 265px; }
  .card--front .band { top: 273px; }
  .card--back .rule { top: 319px; }
  .card--back .band { top: 330px; }

  .contact { position: absolute; left: 0; right: 0; text-align: center; color: #fff; font-size: 20.5px; line-height: 1.2; }
  .contact--phones { top: 40px; display: flex; justify-content: center; align-items: center; gap: 10px; }
  .contact--address { top: 80px; }
  .contact__item { display: inline-flex; align-items: center; gap: 8px; }
  .contact__item + .contact__item { margin-left: 8px; }
  .icon { width: 19px; height: 19px; }
</style>
</head>
<body>

<section class="card card--front">
  <div class="brand">
    <span class="brand__dot"></span>
    <span class="brand__name">Heron Center</span>
  </div>
  <p class="person person__name">Daniel R. Venko, <small>MD</small></p>
  <p class="person person__role">Reconstructive Urology</p>
  <div class="rule"></div>
  <div class="band">
    <div class="contact contact--phones">
      <span class="contact__item">
        <svg class="icon" viewBox="0 0 20 20" aria-label="Phone"><circle cx="10" cy="10" r="8.5" fill="none" stroke="#fff" stroke-width="1.4"/><path d="M7 5.5c-1 1-1 3 1 6s4 3.5 5 2.5l-1.6-1.8-1.2.6c-.8-.4-2-2-2.2-2.8l.9-.9z" fill="#fff"/></svg>
        628-738-2914
      </span>
      <span class="contact__item">
        <svg class="icon" viewBox="0 0 20 20" aria-label="Fax"><rect x="6" y="3" width="8" height="5" fill="none" stroke="#fff" stroke-width="1.4"/><rect x="2" y="8" width="16" height="7" rx="2" fill="#fff"/><rect x="5" y="14" width="10" height="3" fill="#fff"/></svg>
        628-592-8167
      </span>
    </div>
    <p class="contact contact--address">812 Orchard Vale Rd, Suite 4, Larkmoor, CA 94917</p>
  </div>
</section>

<section class="card card--back">
  <div class="brand">
    <span class="brand__dot"></span>
    <span class="brand__name">Heron Center</span>
  </div>
  <div class="rule"></div>
  <div class="band"></div>
</section>

</body>
</html>
```